WEBSITE DESIGN - www.brondellix.com

We need a professional and modern looking website for our business. The current website was only made tentatively and can be viewed (we expect a website MUCH better than this). It needs to be simple and non-cluttered yet look modern and sophisticated. It needs to be very easy to navigate as our tarket market is people over the age of 45. Our logo is attached below and this should be incorporated plus the colours/theme should match this. We don't mind purchasing images online if your design includes these and we like it.

Any other specific questions please enquire as we want to hear them.

Target Market(s)

over 45 age english speaking westerners

Industry/Entity Type

Business

Number of Pages Required

1 page

Requirements
Must have
• -our logo (attached).
• -page tabs as those described (tabs.. but not necessarily each of these pages completed as well although this would be nice).
• -social media logos
• Pages should include: homepage, services, pricing, about us, contact us. There should also be a payments page designed which would link with the other pages but there would be no tab for this.

```html
<!DOCTYPE html>
<html lang="en">
<head>
<meta charset="utf-8">
<title>Brondellix — Instant Support</title>
<link href="https://fonts.googleapis.com/css2?family=Lato:wght@300;400;700;900&family=Open+Sans:ital,wght@0,300;0,400;0,600;1,400&display=swap" rel="stylesheet">
<style>
:root{
  --ink:#222326;
  --dark:#2b2b2d;
  --card-dark:#333335;
  --footer:#3a3a3a;
  --light:#f4f4f4;
  --pale:#efefef;
  --white:#ffffff;
  --muted:#7a7a7a;
  --quote:#9a9a9a;
  --line:#d6d6d6;
  --teal:#7cc4b8;
}
*{margin:0;padding:0;box-sizing:border-box}
html,body{width:1200px;height:3186px;overflow:hidden}
body{font-family:"Open Sans",Arial,sans-serif;color:var(--ink);background:var(--light);position:relative}
section,header,footer{position:absolute;left:0;width:1200px}
.abs{position:absolute}
.center{left:0;width:1200px;text-align:center}
.btn{position:absolute;display:flex;align-items:center;justify-content:center;font-family:"Lato",Arial,sans-serif;font-weight:700;letter-spacing:1.5px;text-transform:uppercase;font-size:11px;border:2px solid currentColor;border-radius:3px}
.heading{font-family:"Lato",Arial,sans-serif;font-weight:700;letter-spacing:3px;text-transform:uppercase}

/* header */
.site-header{top:0;height:76px;background:var(--white);box-shadow:0 1px 4px rgba(0,0,0,.15);z-index:2}
.brand{left:180px;top:20px;display:flex;align-items:center;gap:8px;font-family:"Lato",Arial,sans-serif;font-weight:700;font-size:17px;color:var(--ink)}
.brand-dot{width:22px;height:22px;border-radius:50%;background:var(--ink)}
.nav a{position:absolute;top:36px;font-family:"Lato",Arial,sans-serif;font-weight:700;font-size:10px;letter-spacing:2px;color:var(--ink);text-decoration:none;transform:translateX(-50%)}
.social{left:983px;top:12px;display:flex;gap:9px}
.social span{width:10px;height:10px;border-radius:50%;background:var(--ink)}

/* hero */
.hero{top:76px;height:485px}
.hero-photo{position:absolute;inset:0;background:linear-gradient(90deg,#5a5e66 0%,#8d9097 35%,#a8aab0 60%,#b6b8bd 100%)}
.hero-title{top:157px;font-family:"Lato",Arial,sans-serif;font-weight:700;font-size:38px;color:var(--white)}
.hero-sub{top:222px;font-weight:300;font-size:25px;color:#f0f0f0}
.hero .btn{left:527px;top:292px;width:148px;height:36px;color:var(--white);border-width:1px}

/* about */
.about{top:561px;height:369px;background:var(--light)}
.about h2{top:76px;font-size:18px}
.about p{top:143px;font-size:15px;line-height:26.5px;color:#555}
.about .btn{left:527px;top:250px;width:148px;height:39px;color:var(--ink)}

/* services */
.services{top:930px;height:670px}
.services-photo{position:absolute;inset:0;background:linear-gradient(180deg,#5a6a80 0%,#3f4d60 45%,#283342 100%)}
.services h2{top:54px;font-size:20px;color:var(--white)}
.services .intro{top:103px;font-size:11px;line-height:19px;color:#e4e8ee}
.checklist{left:297px;top:188px;list-style:none}
.checklist li{display:flex;align-items:center;gap:12px;height:34px;font-size:13px;color:var(--white)}
.tagline{top:500px;font-family:"Lato",Arial,sans-serif;font-weight:900;font-size:16px;letter-spacing:.5px;color:var(--white);text-transform:uppercase}
.services .btn{top:574px;height:32px;font-size:9px;color:var(--white);border-width:1px;letter-spacing:1px}

/* mission & vision */
.purpose{top:1600px;height:343px}
.purpose .half{position:absolute;top:0;height:343px}
.mission{left:0;width:600px;background:var(--dark);color:#bdbdbd}
.vision{left:600px;width:600px;background:var(--light);color:#444}
.half h3{position:absolute;top:26px;left:0;width:600px;text-align:center;font-size:18px}
.mission h3{color:var(--white)}
.vision h3{color:var(--ink)}
.half p{position:absolute;left:113px;top:89px;width:374px;text-align:center;font-size:11.5px;line-height:17px}
.half .btn{left:240px;top:276px;width:120px;height:32px;font-size:10px;border-width:1px}
.mission .btn{color:#e0e0e0}
.vision .btn{color:var(--ink)}

/* testimonials */
.testimonials{top:1943px;height:638px;background:var(--pale)}
.testimonials h2{top:77px;font-size:18px}
.testimonials .sub{top:110px;font-size:12px;color:var(--muted)}
.timeline{left:600px;top:181px;width:2px;height:319px;background:var(--line)}
.avatar{width:64px;height:64px;border-radius:50%;border:3px solid var(--white);background:linear-gradient(160deg,#c9c2bb,#6d6661)}
.avatar.teal{background:var(--teal);border:none}
.person{font-family:"Lato",Arial,sans-serif;font-weight:700;font-size:10.5px;letter-spacing:1.5px;text-transform:uppercase;color:var(--ink)}
.person.right{text-align:right;width:300px}
.quote{width:393px;height:100px;background:var(--light);padding:16px 18px;font-style:italic;font-size:12.5px;line-height:21px;color:var(--quote);box-shadow:0 1px 2px rgba(0,0,0,.04)}

/* pricing */
.pricing{top:2581px;height:535px;background:var(--light)}
.pricing h2{top:54px;font-family:"Lato",Arial,sans-serif;font-weight:700;font-size:17px;letter-spacing:.5px}
.plan{position:absolute;top:155px;width:262px;height:259px;text-align:center}
.plan.dark{background:var(--card-dark);color:var(--white)}
.plan.light{background:var(--white);color:var(--ink)}
.plan h4{margin-top:16px;font-family:"Lato",Arial,sans-serif;font-weight:700;font-size:12px;letter-spacing:.5px}
.price{margin-top:11px;font-family:"Lato",Arial,sans-serif;font-weight:900;font-size:34px;line-height:40px}
.price sup{font-size:14px;vertical-align:18px}
.plan ul{list-style:none;text-align:left;margin:6px 0 0 54px}
.plan li{display:flex;align-items:center;gap:9px;height:20px;font-size:11px}
.plan .btn{left:64px;top:212px;width:134px;height:36px;font-family:"Open Sans",Arial,sans-serif;font-weight:400;font-size:12px;letter-spacing:0;border-width:1px}
.plan.dark .btn{color:#d8d8d8}
.plan.light .btn{color:var(--ink);border-color:#999}

/* footer */
.site-footer{top:3116px;height:70px;background:var(--footer);color:#cfcfcf;font-size:11px;display:flex;align-items:center;justify-content:center}
</style>
</head>
<body>

<header class="site-header">
  <div class="brand abs"><span class="brand-dot"></span>Brondellix</div>
  <nav class="nav">
    <a href="#home" style="left:435px">HOMEPAGE</a>
    <a href="#services" style="left:552px">SERVICES</a>
    <a href="#pricing" style="left:665px">PRICING</a>
    <a href="#about" style="left:777px">ABOUT US</a>
    <a href="#contact" style="left:905px">CONTACT US</a>
  </nav>
  <div class="social abs" aria-label="Social media links"><span></span><span></span><span></span></div>
</header>

<section class="hero" id="home">
  <div class="hero-photo" role="img" aria-label="Photo of a smiling support agent wearing a headset in a bright office"></div>
  <h1 class="abs center hero-title">INSTANT SUPPORT</h1>
  <p class="abs center hero-sub">instant technical help for your devices</p>
  <a class="btn">Start a project</a>
</section>

<section class="about" id="about">
  <h2 class="abs center heading">About Us</h2>
  <p class="abs center">Brondellix was established to provide consumers with access to the sophisticated, enterprise-level IT<br>services, support and the benefits and cost savings,available to larger organisations.<br>We provide proactive monitoring and management of customers entire IT needs...</p>
  <a class="btn">Learn more</a>
</section>

<section class="services" id="services">
  <div class="services-photo" role="img" aria-label="Photo of a business meeting around a table in front of a city view window"></div>
  <h2 class="abs center heading">What can we do for you?</h2>
  <p class="abs center intro">The one stop comprehensive diagnostic &amp; repair station for your computer and connected devices.<br>We'll fix anything!</p>
  <ul class="abs checklist">
    <li><svg width="14" height="12" viewBox="0 0 14 12"><path d="M1 6.5l4 4L13 1.5" fill="none" stroke="#fff" stroke-width="2.6"/></svg>Lorem ipsum dolor sit amet</li>
    <li><svg width="14" height="12" viewBox="0 0 14 12"><path d="M1 6.5l4 4L13 1.5" fill="none" stroke="#fff" stroke-width="2.6"/></svg>Lorem ipsum dolor sit amet</li>
    <li><svg width="14" height="12" viewBox="0 0 14 12"><path d="M1 6.5l4 4L13 1.5" fill="none" stroke="#fff" stroke-width="2.6"/></svg>Lorem ipsum dolor sit amet</li>
    <li><svg width="14" height="12" viewBox="0 0 14 12"><path d="M1 6.5l4 4L13 1.5" fill="none" stroke="#fff" stroke-width="2.6"/></svg>Lorem ipsum dolor sit amet</li>
    <li><svg width="14" height="12" viewBox="0 0 14 12"><path d="M1 6.5l4 4L13 1.5" fill="none" stroke="#fff" stroke-width="2.6"/></svg>Lorem ipsum dolor sit amet</li>
    <li><svg width="14" height="12" viewBox="0 0 14 12"><path d="M1 6.5l4 4L13 1.5" fill="none" stroke="#fff" stroke-width="2.6"/></svg>Lorem ipsum dolor sit amet</li>
    <li><svg width="14" height="12" viewBox="0 0 14 12"><path d="M1 6.5l4 4L13 1.5" fill="none" stroke="#fff" stroke-width="2.6"/></svg>Lorem ipsum dolor sit amet</li>
  </ul>
  <p class="abs center tagline">Where technology means business</p>
  <a class="btn" style="left:478px;width:119px">Start a project</a>
  <a class="btn" style="left:605px;width:117px">View details</a>
</section>

<section class="purpose">
  <div class="half mission">
    <h3 class="heading">Mission</h3>
    <p>Nam ut eros suscipit, tincidunt erat eget, placerat nisi. Vivamus cursus auctor massa a lacinia. Praesent vitae arcu sollicitudin, dapibus nibh quis, aliquam ligula. Fusce finibus ultricies sem vitae venenatis. Suspendisse convallis dapibus libero lobortis rutrum. Suspendisse vel accumsan lectus. Sed tempor ipsum non ultricies placerat. Ut ultricies, lectus non eleifend pharetra, mauris quam dictum mi, eget semper neque felis a ligula. Etiam pellentesque lacus lectus, eget blandit quam auctor vel. Quisque aliquam pharetra fringilla. Sed sollicitudin tincidunt volutpat.</p>
    <a class="btn">View all</a>
  </div>
  <div class="half vision">
    <h3 class="heading">Vision</h3>
    <p>Nam ut eros suscipit, tincidunt erat eget, placerat nisi. Vivamus cursus auctor massa a lacinia. Praesent vitae arcu sollicitudin, dapibus nibh quis, aliquam ligula. Fusce finibus ultricies sem vitae venenatis. Suspendisse convallis dapibus libero lobortis rutrum. Suspendisse vel accumsan lectus. Sed tempor ipsum non ultricies placerat. Ut ultricies, lectus non eleifend pharetra, mauris quam dictum mi, eget semper neque felis a ligula. Etiam pellentesque lacus lectus, eget blandit quam auctor vel. Quisque aliquam pharetra fringilla. Sed sollicitudin tincidunt volutpat.</p>
    <a class="btn">View all</a>
  </div>
</section>

<section class="testimonials">
  <h2 class="abs center heading">Happy Customers</h2>
  <p class="abs center sub">what do our customers think</p>
  <div class="abs timeline"></div>

  <p class="abs person right" style="left:252px;top:2190px;top:190px">Dorian Hale</p>
  <div class="abs avatar" style="left:569px;top:164px" role="img" aria-label="Customer portrait"></div>
  <p class="abs quote" style="left:646px;top:166px">Vivamus sagittis lacus augue laoreet rutrum faucibus dolor auctor. Sed posuere consectetur est at lobortis. Cras justo odio, dapibus ac facilisis in, egestas eget quam.</p>

  <p class="abs quote" style="left:161px;top:315px">Aenean lacinia bibendum nulla sed consectetur. Nulla vitae elit libero, a pharetra augue. Duis mollis, est non commodo luctus, nisi erat porttitor ligula, eget lacinia odio sem nec elit.</p>
  <div class="abs avatar" style="left:569px;top:313px" role="img" aria-label="Customer portrait"></div>
  <p class="abs person" style="left:648px;top:338px">Marten Ovelle</p>

  <p class="abs person right" style="left:252px;top:479px">Quentin Raskell</p>
  <div class="abs avatar teal" style="left:569px;top:453px"></div>
  <p class="abs quote" style="left:646px;top:457px">Fusce dapibus, tellus ac cursus commodo, tortor mauris condimentum nibh, ut fermentum massa justo sit amet risus. Lorem ipsum dolor sit amet, consectetur adipiscing elit. Donec</p>
</section>

<section class="pricing" id="pricing">
  <h2 class="abs center">PRICING AND PLANS</h2>

  <div class="plan dark" style="left:178px">
    <h4>1 MONTH MEMBERSHIP</h4>
    <p class="price">$33<sup>.33</sup></p>
    <ul>
      <li><svg width="10" height="9" viewBox="0 0 14 12"><path d="M1 6.5l4 4L13 1.5" fill="none" stroke="currentColor" stroke-width="3"/></svg>Lorem ipsum dolor sit amet</li>
      <li><svg width="10" height="9" viewBox="0 0 14 12"><path d="M1 6.5l4 4L13 1.5" fill="none" stroke="currentColor" stroke-width="3"/></svg>Lorem ipsum dolor sit amet</li>
      <li><svg width="10" height="9" viewBox="0 0 14 12"><path d="M1 6.5l4 4L13 1.5" fill="none" stroke="currentColor" stroke-width="3"/></svg>Lorem ipsum dolor sit amet</li>
      <li><svg width="10" height="9" viewBox="0 0 14 12"><path d="M1 6.5l4 4L13 1.5" fill="none" stroke="currentColor" stroke-width="3"/></svg>Lorem ipsum dolor sit amet</li>
      <li><svg width="10" height="9" viewBox="0 0 14 12"><path d="M1 6.5l4 4L13 1.5" fill="none" stroke="currentColor" stroke-width="3"/></svg>Lorem ipsum dolor sit amet</li>
    </ul>
    <a class="btn">BUY NOW</a>
  </div>

  <div class="plan light" style="left:469px">
    <h4>6 MONTHS MEMBERSHIP</h4>
    <p class="price">$59<sup>.00</sup></p>
    <ul>
      <li><svg width="10" height="9" viewBox="0 0 14 12"><path d="M1 6.5l4 4L13 1.5" fill="none" stroke="currentColor" stroke-width="3"/></svg>Lorem ipsum dolor sit amet</li>
      <li><svg width="10" height="9" viewBox="0 0 14 12"><path d="M1 6.5l4 4L13 1.5" fill="none" stroke="currentColor" stroke-width="3"/></svg>Lorem ipsum dolor sit amet</li>
      <li><svg width="10" height="9" viewBox="0 0 14 12"><path d="M1 6.5l4 4L13 1.5" fill="none" stroke="currentColor" stroke-width="3"/></svg>Lorem ipsum dolor sit amet</li>
      <li><svg width="10" height="9" viewBox="0 0 14 12"><path d="M1 6.5l4 4L13 1.5" fill="none" stroke="currentColor" stroke-width="3"/></svg>Lorem ipsum dolor sit amet</li>
      <li><svg width="10" height="9" viewBox="0 0 14 12"><path d="M1 6.5l4 4L13 1.5" fill="none" stroke="currentColor" stroke-width="3"/></svg>Lorem ipsum dolor sit amet</li>
    </ul>
    <a class="btn">BUY NOW</a>
  </div>

  <div class="plan dark" style="left:760px">
    <h4>12 MONTHS MEMBERSHIP</h4>
    <p class="price">$120<sup>.00</sup></p>
    <ul>
      <li><svg width="10" height="9" viewBox="0 0 14 12"><path d="M1 6.5l4 4L13 1.5" fill="none" stroke="currentColor" stroke-width="3"/></svg>Lorem ipsum dolor sit amet</li>
      <li><svg width="10" height="9" viewBox="0 0 14 12"><path d="M1 6.5l4 4L13 1.5" fill="none" stroke="currentColor" stroke-width="3"/></svg>Lorem ipsum dolor sit amet</li>
      <li><svg width="10" height="9" viewBox="0 0 14 12"><path d="M1 6.5l4 4L13 1.5" fill="none" stroke="currentColor" stroke-width="3"/></svg>Lorem ipsum dolor sit amet</li>
      <li><svg width="10" height="9" viewBox="0 0 14 12"><path d="M1 6.5l4 4L13 1.5" fill="none" stroke="currentColor" stroke-width="3"/></svg>Lorem ipsum dolor sit amet</li>
      <li><svg width="10" height="9" viewBox="0 0 14 12"><path d="M1 6.5l4 4L13 1.5" fill="none" stroke="currentColor" stroke-width="3"/></svg>Lorem ipsum dolor sit amet</li>
    </ul>
    <a class="btn">BUY NOW</a>
  </div>
</section>

<footer class="site-footer" id="contact">© 2016 Brondellix. All rights reserved.</footer>

</body>
</html>
```